I want to thank you very much for all your great designs. It was a really tough choice, but I have finally chosen a winner. I have been very happy with this process and very pleased with all the great choices I was given. I will definitely refer this company to my friends and tell them that they will get exactly what they are looking for from many, very talented designers. Thanks again! Dana
Hello All.
When doing that additional return address label,
Include:
- Logo
- Company Name
- Address
- Design Concept
- Size: 4"X3" (inches) return label
Thanks
Hello Designers! Great work that I'm seeing! If I have starred one of your designs, you should have received private messages regarding them by now. If not, please message me.
Can you please be sure to resubmit those designs with the changes I have requested because if I starred it, I'm considering it as my choice.
Don't forget to review the general comments in case I didn't add those things in your private messages.
One thing I wanted to add to the general comments is the fact that I somehow want "The Builder's Coverage Advisors" to be incorporated large on the back of the cards.
After I get the updated designs and I will re-star them. I would then like to start receiving the stationery layouts from the top designs I pick. Besides the letterhead and #10 return envelope I will also need a design for a return address label/sticker for a large 9X11 envelope.
Thanks for your participation. I look for to the updated designs. Dana
Hi. Thanks so much for all your designs. Just a couple of general comments.
I do like the more colorful cards using the gold as an accent only. I prefer the blue and black and white more for large sections or entire backgrounds.
I would like either spaces or periods between all the phone numbers, please. example: 555.418.3927 or 555 418 3927
License number can simply be License# .......
I haven't decided if I like the symbols next to the phone, fax, email, web yet. Can I see some different options instead of symbols so I can decide.
Thanks again for your time and great work. I look forward to choosing the winning design. Dana
I haven't decided if I like the symbols next to the phone, fax, email, web. Can I see some different options instead of symbols.
Thanks for your time and great work. I look forward to choosing the winning design. Dana
RT/PHW/NC Team
#8 I like this one too. Like the added info on back. Also can you please add the license number so I can see that on there. We have to advertise our insurance license for the company and individuals. Thanks
#2 I like this design. Please add & refer to the information requested on card in the design request area and the comments section for information on what info I want on the back. I'd like to see it with all my data, please. Please also add spacing or characters on the phone numbers. Thanks so much.

```html
<!DOCTYPE html>
<html lang="en">
<head>
<meta charset="utf-8">
<title>Halvern Insurance Stationery</title>
<link href="https://fonts.googleapis.com/css2?family=Open+Sans:wght@400;600;700&display=swap" rel="stylesheet">
<style>
:root{
  --bg:#ffffff;
  --paper:#ffffff;
  --ink:#1d1f22;
  --dark:#16181b;
  --blue:#1f7bc1;
  --blue-deep:#0d4f86;
  --blue-light:#6fb3e3;
  --gold:#c9a14a;
  --grey:#8a9097;
  --faint:#f0f2f5;
}
*{margin:0;padding:0;box-sizing:border-box}
html,body{width:1200px;height:230px;overflow:hidden;background:var(--bg);font-family:"Open Sans",sans-serif;color:var(--ink)}
.canvas{position:relative;width:1200px;height:230px}
.piece{position:absolute;box-shadow:0 1px 4px rgba(0,0,0,.3);overflow:hidden;background:var(--paper)}
.brand{font-weight:700;font-size:6px;line-height:1;white-space:nowrap;display:flex;align-items:center;gap:3px;color:var(--ink)}
.brand .dot{width:5px;height:5px;border-radius:50%;background:var(--blue);flex:none}
.brand.light{color:#fff}
.tiny{font-size:3.5px;line-height:1.4;color:var(--grey);white-space:nowrap}
.tiny.light{color:#cfd5db}

/* business cards */
.card{width:68px;height:40px}
.card.dark{background:var(--dark)}
.card.blue{background:linear-gradient(135deg,var(--blue),var(--blue-deep))}
.card .inner{position:absolute;left:6px;top:6px;right:5px}
.card .band{position:absolute;left:0;right:0;bottom:0;height:5px;background:linear-gradient(90deg,var(--blue-deep),var(--blue))}
.card .accent{position:absolute;left:0;right:0;bottom:5px;height:1px;background:var(--gold)}
.card .tagline{font-size:4px;font-weight:600;color:#fff;margin-top:6px;white-space:nowrap}
.card .name{font-size:4.5px;font-weight:700;margin-top:5px}

/* letterheads */
.letter{width:144px;height:206px;top:14px}
.letter .head{position:absolute;left:10px;top:10px}
.letter .mark{position:absolute;left:32px;top:62px;width:80px;height:80px;border-radius:50%;background:var(--faint)}
.letter .contact{position:absolute;right:8px;bottom:14px;text-align:right}
.letter .footline{position:absolute;left:0;right:0;bottom:8px;height:1px;background:var(--gold)}
.letter .foot{position:absolute;left:0;right:0;bottom:0;height:8px;background:linear-gradient(90deg,var(--blue-deep),var(--blue),var(--blue-light))}

/* envelopes */
.envelope .flap{position:absolute;inset:0}
.envelope .band{position:absolute;left:0;right:0;bottom:0;height:4px;background:linear-gradient(90deg,var(--blue-deep),var(--blue))}
</style>
</head>
<body>
<div class="canvas">

  <!-- business cards -->
  <div class="piece card dark" style="left:12px;top:46px">
    <div class="inner"><div class="brand light"><span class="dot"></span>Halvern Insurance</div>
      <div class="tagline">The Builder's Coverage Advisors</div></div>
    <div class="accent"></div><div class="band"></div>
  </div>
  <div class="piece card" style="left:86px;top:46px">
    <div class="inner"><div class="brand"><span class="dot"></span>Halvern Insurance</div>
      <div class="name">Dana</div><div class="tiny">RT/PHW/NC Team<br>555.418.3927</div></div>
    <div class="accent"></div><div class="band"></div>
  </div>
  <div class="piece card blue" style="left:12px;top:96px">
    <div class="inner"><div class="brand light"><span class="dot" style="background:#fff"></span>Halvern Insurance</div>
      <div class="tagline">The Builder's Coverage Advisors</div></div>
  </div>
  <div class="piece card" style="left:86px;top:96px">
    <div class="inner"><div class="brand"><span class="dot"></span>Halvern Insurance</div>
      <div class="name">Dana</div><div class="tiny">dana@halverninsure.com<br>555 418 3927</div></div>
    <div class="accent"></div><div class="band"></div>
  </div>
  <div class="piece card dark" style="left:12px;top:146px">
    <div class="inner"><div class="brand light"><span class="dot"></span>Halvern Insurance</div>
      <div class="tiny light" style="margin-top:5px">License# on file<br>halverninsure.com</div></div>
    <div class="band"></div>
  </div>
  <div class="piece card" style="left:86px;top:146px">
    <div class="inner"><div class="brand"><span class="dot"></span>Halvern Insurance</div>
      <div class="tiny" style="margin-top:5px">12 Harbor Road<br>Lakeport, ME</div></div>
    <div class="band"></div>
  </div>

  <!-- letterheads -->
  <div class="piece letter" style="left:180px">
    <div class="head brand"><span class="dot"></span>Halvern Insurance</div>
    <div class="mark"></div>
    <div class="contact tiny">12 Harbor Road, Lakeport, ME<br>555.418.3927</div>
    <div class="footline"></div><div class="foot"></div>
  </div>
  <div class="piece letter" style="left:356px">
    <div class="head brand"><span class="dot"></span>Halvern Insurance</div>
    <div class="mark"></div>
    <div class="contact tiny">12 Harbor Road, Lakeport, ME<br>555.418.3927</div>
    <div class="footline"></div><div class="foot"></div>
  </div>
  <div class="piece letter" style="left:516px">
    <div class="head brand"><span class="dot"></span>Halvern Insurance</div>
    <div class="mark"></div>
    <div class="contact tiny">12 Harbor Road, Lakeport, ME<br>555.418.3927</div>
    <div class="footline"></div><div class="foot"></div>
  </div>
  <div class="piece letter" style="left:676px">
    <div class="head brand"><span class="dot"></span>Halvern Insurance</div>
    <div class="mark"></div>
    <div class="contact tiny">12 Harbor Road, Lakeport, ME<br>555.418.3927</div>
    <div class="footline"></div><div class="foot"></div>
  </div>

  <!-- #10 envelopes -->
  <div class="piece envelope" style="left:834px;top:58px;width:150px;height:46px">
    <div style="position:absolute;left:0;right:0;top:0;height:20px;background:var(--dark)"></div>
    <div class="brand light" style="position:absolute;left:6px;top:7px"><span class="dot"></span>Halvern Insurance</div>
    <div class="band"></div>
  </div>
  <div class="piece envelope" style="left:834px;top:138px;width:150px;height:46px">
    <div class="brand" style="position:absolute;left:6px;top:7px"><span class="dot"></span>Halvern Insurance</div>
    <div class="tiny" style="position:absolute;left:14px;top:15px">12 Harbor Road, Lakeport, ME</div>
    <div class="band"></div>
  </div>

  <div class="piece envelope" style="left:1000px;top:58px;width:190px;height:58px">
    <svg class="flap" viewBox="0 0 190 58" preserveAspectRatio="none" aria-hidden="true">
      <polygon points="0,0 190,0 95,30" fill="#16181b"/>
      <polyline points="0,0 95,30 190,0" fill="none" stroke="#1f7bc1" stroke-width="2"/>
    </svg>
    <div class="brand" style="position:absolute;left:8px;bottom:8px"><span class="dot"></span>Halvern Insurance</div>
  </div>
  <div class="piece envelope" style="left:1000px;top:138px;width:190px;height:58px">
    <svg class="flap" viewBox="0 0 190 58" preserveAspectRatio="none" aria-hidden="true">
      <polyline points="0,0 95,26 190,0" fill="none" stroke="#c5ccd3" stroke-width="1"/>
    </svg>
    <div class="brand" style="position:absolute;left:8px;bottom:10px"><span class="dot"></span>Halvern Insurance</div>
    <div class="band"></div>
  </div>

</div>
</body>
</html>
```